Photographer Card

I'm currently doing freelance photography and i need a creative design name card especially when i attend events.
I require a design that makes a STATEMENT.
Simple, elegant and nothing like the usual name cards ive seen around (Example: with a camera/tripod etc in the design).

Photographer: Dorian VP
Mobile: +65 84126957
E-mail: Dorian.VP.Photography@mailvista.net
Friendlane: www.friendlane.net/dorian.vp.photography

Thanks for your time and hope it will turn out well! :)
Updates

Thanks for all your inputs!

Im liking the cursive feel.

Id prefer not to include the title "freelance"  :)

Also, im looking for a logo to establish myself

http://www.artmosaic.net/art/Cotton-Business-Card-583021746

Hi all! Thanks for the designs

"Capturing magical moments"
"Capturing magical moments that are gone forever"

Back design can be in big font "look HERE"

Maybe with focusing box 

Names can be played with horizontal and vertical.

Industry/Entity Type

Camera

Font styles to use
Script

```html
<!DOCTYPE html>
<html lang="en">
<head>
<meta charset="utf-8">
<title>Dorian VP — Photographer Business Card</title>
<link rel="stylesheet" href="https://fonts.googleapis.com/css2?family=PT+Sans&display=swap">
<style>
  :root {
    --paper: #ffffff;
    --card-black: #0a0a0a;
    --accent-orange: #f7941d;
    --rule-bronze: #6b4214;
    --rule-dark: #4a3212;
  }
  html, body {
    margin: 0;
    padding: 0;
    width: 1200px;
    height: 322px;
    overflow: hidden;
    background: var(--paper);
  }
  .canvas {
    position: relative;
    width: 1200px;
    height: 322px;
    background: var(--paper);
  }
  .card {
    position: absolute;
    top: 0;
    width: 564px;
    height: 322px;
    background: var(--card-black);
  }
  .card--front { left: 29px; }
  .card--back { left: 636px; }
  .card svg {
    display: block;
    width: 564px;
    height: 322px;
  }
  .brand-name,
  .brand-title,
  .contact-line {
    font-family: "PT Sans", "Myriad Pro", sans-serif;
    fill: var(--accent-orange);
  }
  .brand-name { font-size: 68px; letter-spacing: 1px; }
  .brand-title { font-size: 25px; letter-spacing: 9.6px; }
  .contact-line { font-size: 23.5px; }
  .contact-line--small { font-size: 21px; }
  .brand-rule { stroke: var(--rule-bronze); stroke-width: 1; }
  .footer-rule { stroke: var(--rule-dark); stroke-width: 1; }
</style>
</head>
<body>
<div class="canvas">
  <section class="card card--front" aria-label="Card front">
    <svg viewBox="0 0 564 322" xmlns="http://www.w3.org/2000/svg">
      <text class="brand-name" x="551" y="156" text-anchor="end">DORIAN VP</text>
      <line class="brand-rule" x1="174" y1="166.5" x2="552" y2="166.5"/>
      <text class="brand-title" x="561" y="200" text-anchor="end">PHOTOGRAPHER</text>
    </svg>
  </section>

  <section class="card card--back" aria-label="Card back">
    <svg viewBox="0 0 564 322" xmlns="http://www.w3.org/2000/svg">
      <text class="contact-line" x="14" y="99">Dorian VP</text>
      <text class="contact-line" x="14" y="131">Photographer</text>
      <text class="contact-line" x="14" y="163">Mobile:&#160; +65 84126957</text>
      <text class="contact-line" x="14" y="196" textLength="428" lengthAdjust="spacingAndGlyphs">E-mail: Dorian.VP.Photography@mailvista.net</text>
      <text class="contact-line contact-line--small" x="14" y="225" textLength="542" lengthAdjust="spacingAndGlyphs">Friendlane: www.friendlane.net/dorian.vp.photography</text>
      <line class="footer-rule" x1="0" y1="266.5" x2="564" y2="266.5"/>
    </svg>
  </section>
</div>
</body>
</html>
```